Sexy stockings - 1 creative web page design needed!

We need a design for the main home page of our company 'Lumera Hosiery'. Out company sells stockings for women in Australia and this will be an online shopping site.

I have mocked up an example showing the type of layout and text that is required:
http://www.lumerahosiery.com.au

The design should have the same menu and text as shown in the example. A slider will be positioned in the middle of the page promoting certain styles.

The page currently has a width of 800px.

What I am looking for is some genuine design flare. Good use of fonts, stylish menu and interesting background. Also please note, this is the will be the home page so please keep text to a minimum.

An example of stylish menus can be seen here: (See 22, 26, 41)
http://pixelgroveblog.com/design-showcase-inspiration/50-stylish-navigation-menus-for-design-inspiration/

An example of creative footers:
http://www.fadrunel.com/2009/01/40-nice-and-creative-website-footer-designs/

(See 22, 26, 41)

Update: I would like a banner picture at the top with the logo and title overlaid. Also some areas where I could advertise specials and 1 day delivery in the Metro area.

Only one page is required to be designed. No coding of links, slider etc is needed.

The deliverable will be one photoshop project file.
Updates

So far the designs submitted have not been very creative. I am not interested in a plain design where you have just copy and pasted the pictures I  have supplied and changed the background colour - I could do this myself in Photoshop. What I am looking for is some genuine design flare. Good use of fonts, stylish menu and interesting background.

Also note - this is a home page, so there should be minimal text. 

Once a quality design has been submitted, I will guarantee this project.

Reason: I have extended the deadline in order for designers to submit their new designs for the following update to the brief: I have decided a banner picture at the top with the logo and title overlaid would look great. Also can I have some areas on the page where I could advertise specials and 1 day delivery in the Metro area.

Target Market(s)

We are marketing this product to the sophisticated professional woman.

Industry/Entity Type

Online Shopping

Requirements
Must have
• Must have the subtitle - "Signature Italian Stockings"

Logo picture incorporated somewhere on page. (Do not include "Sheer Silky Stockings" from packaging.)

The style of the webpage should be consistent with the packaging.

Nice to have
• A creative background pattern - maybe incorporate the logo.
Should not have
• I am looking for a CREATIVE design, do not submit a design that has is just the supplied pictures copy and pasted in a different layout. (I could easily do that myself).

```html
<!DOCTYPE html>
<html lang="en">
<head>
<meta charset="utf-8">
<title>Lumera Hosiery – Home</title>
<link href="https://fonts.googleapis.com/css2?family=Cormorant+Garamond:wght@500&family=Montserrat:wght@400;700&family=PT+Sans:wght@400&display=swap" rel="stylesheet">
<style>
  :root{
    --charcoal:#4b4a4f;
    --ink:#333236;
    --heading:#57565b;
    --blush:#f0b6bb;
    --berry:#b0173f;
    --mauve:#8c6c78;
    --paper:#ffffff;
    --arrow-bg:#dfe4e6;
  }
  *{box-sizing:border-box;margin:0;padding:0}
  html,body{width:1200px;height:1100px;overflow:hidden;background:var(--paper)}
  body{position:relative;font-family:"PT Sans",sans-serif;color:var(--ink)}
  .top-strip{position:absolute;left:0;top:0;width:1200px;height:14px;background:var(--charcoal);border-bottom:3px solid var(--blush)}
  .header-backdrop{position:absolute;left:0;top:17px;width:1200px;height:455px;
    background:linear-gradient(to bottom,#e6e4e5 0%,#f4f3f3 25%,#ffffff 38%,#f1f0f0 62%,#dcdadb 96%,#ffffff 100%)}
  .brand{position:absolute;left:182px;top:28px;display:flex;align-items:center;gap:12px}
  .brand-mark{width:100px;height:100px;border-radius:50%;background:var(--mauve)}
  .brand-name{font-family:"Cormorant Garamond",serif;font-weight:500;font-size:40px;color:var(--ink);white-space:nowrap}
  .brand-divider{position:absolute;left:562px;top:38px;width:8px;height:74px;background:var(--blush)}
  .subtitle{position:absolute;left:582px;top:46px;font-family:"Montserrat",sans-serif;font-size:12.5px;line-height:20px;letter-spacing:2.6px;color:var(--ink);white-space:nowrap}
  .subtitle .strong{font-weight:700}
  .main-nav{position:absolute;left:704px;top:60px;width:318px;height:32px;
    border-top:1px solid #fff;border-bottom:1px solid #fff;background:rgba(255,255,255,0.55);
    display:flex;align-items:center;font-family:"Montserrat",sans-serif;font-size:14px;color:var(--heading);white-space:nowrap}
  .main-nav span{display:block;flex:none}
  .main-nav .sep{color:#b9b8ba;font-size:12px}
  .slider{position:absolute;left:185px;top:144px;width:831px;height:363px;border:4px solid var(--blush);border-radius:4px;overflow:hidden}
  .slide-photo{position:absolute;inset:0;background:linear-gradient(90deg,#e9e8e8 0%,#3a3539 14%,#f3f3f3 30%,#2c2a2d 45%,#f1f1f1 60%,#1f1e20 74%,#f2f2f2 90%,#e8e8e8 100%)}
  .slide-arrow{position:absolute;top:162px;width:38px;height:38px;border-radius:50%;background:var(--arrow-bg)}
  .slide-arrow.prev{left:12px}
  .slide-arrow.next{right:12px}
  .slide-arrow svg{position:absolute;left:11px;top:11px}
  .slide-caption{position:absolute;left:0;bottom:0;width:100%;height:31px;background:rgba(70,70,74,0.82);
    font-family:"Montserrat",sans-serif;font-size:15px;color:#fff;line-height:31px;padding-left:20px;white-space:nowrap}
  .slide-dots{position:absolute;right:10px;bottom:5px;display:flex;gap:4px}
  .slide-dots span{width:21px;height:21px;border:1px solid #fff;background:#d9d8d8;color:var(--ink);
    font-family:"Montserrat",sans-serif;font-size:12px;text-align:center;line-height:19px}
  .slide-dots span.active{background:var(--berry);color:#fff}
  .section-title{position:absolute;top:530px;font-family:"Montserrat",sans-serif;font-size:20px;font-weight:400;color:var(--heading);letter-spacing:0.2px;white-space:nowrap}
  .collections-photo{position:absolute;left:212px;top:570px;width:278px;height:155px;
    background:linear-gradient(90deg,#fff 0%,#4a3f45 12%,#fff 30%,#4a3f45 44%,#fff 62%,#4a3f45 76%,#fff 94%)}
  .mini-arrow{position:absolute;top:640px}
  .box-photo{position:absolute;left:540px;top:575px;width:215px;height:160px;
    background:linear-gradient(160deg,#fff 8%,#4c4a50 30%,#5a585e 55%,#dcb2b0 75%,#fff 95%)}
  .copy{position:absolute;font-size:10.6px;line-height:14.1px;color:var(--ink)}
  .footer{position:absolute;left:0;top:966px;width:1200px;height:134px;background:var(--charcoal);border-top:3px solid var(--blush);color:#fff}
  .contact-line{position:absolute;top:18px;display:flex;align-items:center;gap:18px;font-family:"Montserrat",sans-serif;font-size:14.5px;white-space:nowrap}
  .address{position:absolute;left:183px;top:53px;font-family:"Montserrat",sans-serif;font-size:16.5px;line-height:21px}
  .footer-nav{position:absolute;left:713px;top:21px;font-family:"Montserrat",sans-serif;font-size:17px;word-spacing:2px;white-space:nowrap}
  .footer-nav .sep{margin:0 12px}
</style>
</head>
<body>
  <div class="top-strip"></div>
  <div class="header-backdrop" role="img" aria-label="Soft grey paisley background pattern"></div>

  <div class="brand">
    <div class="brand-mark"></div>
    <div class="brand-name">Lumera Hosiery</div>
  </div>
  <div class="brand-divider"></div>
  <div class="subtitle">SIGNATURE<br>ITALIAN<br><span class="strong">STOCKINGS</span></div>

  <nav class="main-nav">
    <span style="margin-left:3px">COLLECTION</span>
    <span class="sep" style="margin-left:14px">|</span>
    <span style="margin-left:26px">NEWS</span>
    <span class="sep" style="margin-left:40px">|</span>
    <span style="margin-left:13px">ABOUT US</span>
  </nav>

  <section class="slider">
    <div class="slide-photo" role="img" aria-label="Three models wearing lace and sheer black stockings"></div>
    <div class="slide-arrow prev"><svg width="16" height="16" viewBox="0 0 16 16"><path d="M10.5 2 L4.5 8 L10.5 14" fill="none" stroke="#3d3d42" stroke-width="3"/></svg></div>
    <div class="slide-arrow next"><svg width="16" height="16" viewBox="0 0 16 16"><path d="M5.5 2 L11.5 8 L5.5 14" fill="none" stroke="#3d3d42" stroke-width="3"/></svg></div>
    <div class="slide-caption">Lorem ipsum dolor sit amet, consectetur adipiscing elit. Maecenas in aliquam tellus.</div>
    <div class="slide-dots"><span class="active">1</span><span>2</span><span>3</span><span>4</span></div>
  </section>

  <h2 class="section-title" style="left:188px">COLLECTIONS</h2>
  <h2 class="section-title" style="left:528px">SIGNATURE BOX</h2>
  <h2 class="section-title" style="left:813px">BLOG</h2>

  <svg class="mini-arrow" style="left:190px" width="12" height="14" viewBox="0 0 12 14"><path d="M9 1 L3 7 L9 13" fill="none" stroke="var(--blush)" stroke-width="3"/></svg>
  <div class="collections-photo" role="img" aria-label="Three pairs of legs in floral lace stockings"></div>
  <svg class="mini-arrow" style="left:499px" width="12" height="14" viewBox="0 0 12 14"><path d="M3 1 L9 7 L3 13" fill="none" stroke="var(--blush)" stroke-width="3"/></svg>

  <div class="box-photo" role="img" aria-label="Open charcoal and pink signature gift box"></div>

  <p class="copy" style="left:813px;top:561px;width:185px">Lorem ipsum dolor sit amet, consectetur adipiscing elit. Maecenas in aliquam tellus. Mauris cursus fermentum turpis in condi-mentum. Nam sollicitudin gravida lorem, non posuere nisl luctus ac. Lorem ipsum dolor sit amet, consectetur adipiscing elit. Morbi at arcu neque, vel egestas risus. Phasellus sodales porta luctus. Nulla mattis arcu id leo tincidunt congue. Morbi consectetur luctus leo, nec hendrerit felis consequat eu. Etiam</p>

  <p class="copy" style="left:201px;top:761px;width:298px">Lorem ipsum dolor sit amet, consectetur adipiscing elit. Maecenas in aliquam tellus. Mauris cursus fermentum turpis in condimentum. Nam sollicitudin gravida lorem, non posuere nisl luctus ac. Lorem ipsum dolor sit amet, consectetur adipiscing elit. Morbi at arcu neque, vel egestas risus. Phasellus sodales porta luctus. Nulla mattis arcu id leo tincidunt congue. Morbi consectetur luctus leo, nec hendrerit felis consequat eu. Etiam placerat facilisis justo a porta. Phasellus adipiscing, purus eu ultricies bibendum, nibh magna ornare felis, a scelerisque sem est ac dolor. Vestibulum ante ipsum primis in faucibus orci luctus et ultrices posuere cubilia Curae;</p>

  <p class="copy" style="left:557px;top:761px;width:185px">Lorem ipsum dolor sit amet, consectetur adipiscing elit. Maecenas in aliquam tellus. Mauris cursus fermentum turpis in condi-mentum. Nam sollicitudin gravida lorem, non posuere nisl luctus ac. Lorem ipsum dolor sit amet, consectetur adipiscing elit. Morbi at arcu neque, vel egestas risus. Phasellus sodales porta luctus. Nulla mattis arcu id leo tincidunt congue. Morbi consectetur luctus leo, nec hendrerit felis consequat eu. Etiam</p>

  <p class="copy" style="left:813px;top:761px;width:185px">Lorem ipsum dolor sit amet, consectetur adipiscing elit. Maecenas in aliquam tellus. Mauris cursus fermentum turpis in condi-mentum. Nam sollicitudin gravida lorem, non posuere nisl luctus ac. Lorem ipsum dolor sit amet, consectetur adipiscing elit. Morbi at arcu neque, vel egestas risus. Phasellus sodales porta luctus. Nulla mattis arcu id leo tincidunt congue. Morbi consectetur luctus leo, nec hendrerit felis consequat eu. Etiam</p>

  <footer class="footer">
    <div class="contact-line" style="left:180px">
      <svg width="22" height="22" viewBox="0 0 24 24"><path d="M6.6 2.5c.6-.3 1.3-.1 1.6.5l2 3.6c.3.6.2 1.3-.3 1.7l-1.5 1.2c1 2.3 2.8 4.2 5.1 5.3l1.3-1.5c.4-.5 1.100-.6 1.700-.3l3.6 2c.6.3.8 1 .5 1.6l-1.2 2.3c-.4.7-1.2 1.1-2 1C9.8 19.2 4.4 13.8 3.7 6.2c-.1-.8.3-1.6 1-2z" fill="#d8d8da"/></svg>
      <span>000*000*000</span>
    </div>
    <div class="contact-line" style="left:356px">
      <svg width="28" height="20" viewBox="0 0 28 20"><rect x="1" y="1" width="26" height="18" rx="2" fill="#d8d8da"/><path d="M2 2 L14 11 L26 2" fill="none" stroke="#7a797d" stroke-width="1.5"/></svg>
      <span>anyemail@email.com</span>
    </div>
    <div class="address">1234 Any Address<br>Any State, Any County</div>
    <div class="footer-nav">COLLECTION<span class="sep">|</span>NEWS<span class="sep">|</span>ABOUT US</div>
  </footer>
</body>
</html>
```